Trevolant Consulting Card Design

Create a card design for the company.

Target Market(s)

B2B

Industry/Entity Type

Management Consulting

Contact Information for Business Card

Name; Role; email; phone; website;

Colors
0555a3
3276b5
85abd2
cee9f5

```html
<!DOCTYPE html>
<html lang="en">
<head>
<meta charset="utf-8">
<title>Trevolant Consulting – Business Card</title>
<link rel="stylesheet" href="https://fonts.googleapis.com/css2?family=Open+Sans:wght@400;600;700;800&display=swap">
<style>
  :root {
    --stage: #000000;
    --brand-deep: #0555a3;
    --brand-mid: #3276b5;
    --brand-light: #85abd2;
    --brand-sky: #cee9f5;
    --bright-blue: #0aa3e3;
    --band-top: #1a6fc0;
    --white: #ffffff;
    --ink-grey: #6d6e70;
    --tag-grey: #8a8c8f;
    --tag-light: #cfd3d8;
  }
  * { margin: 0; padding: 0; box-sizing: border-box; }
  html, body {
    width: 1200px; height: 1000px; overflow: hidden;
    background: var(--stage);
    font-family: "Open Sans", Arial, sans-serif;
  }
  .canvas { position: relative; width: 1200px; height: 1000px; }

  .card { position: absolute; left: 286px; width: 628px; overflow: hidden; }

  /* Front */
  .card-front {
    top: 130px; height: 357px;
    background: linear-gradient(200deg, var(--bright-blue) 0%, #1080d4 40%, var(--brand-deep) 100%);
  }
  .front-lockup { position: absolute; left: 242px; top: 146px; }
  .front-lockup .wordmark {
    display: block;
    font-weight: 800; font-size: 54px; line-height: 1;
    color: var(--white); letter-spacing: -0.5px;
  }
  .front-lockup .tagline {
    display: block; margin-top: 5px;
    font-weight: 600; font-size: 17px; line-height: 1; letter-spacing: 0.6px;
    color: var(--tag-light);
  }

  /* Back */
  .card-back { top: 525px; height: 358px; background: var(--white); }
  .back-lockup { position: absolute; left: 132px; top: 52px; }
  .back-lockup .wordmark {
    display: block;
    font-weight: 800; font-size: 38px; line-height: 1;
    color: var(--brand-deep); letter-spacing: -0.4px;
  }
  .back-lockup .tagline {
    display: block; margin-top: 4px;
    font-weight: 600; font-size: 12.5px; letter-spacing: 0.5px;
    color: var(--tag-grey);
  }
  .holder { position: absolute; right: 22px; top: 100px; text-align: right; }
  .holder .name {
    display: block; font-size: 24px; line-height: 1.05;
    color: var(--ink-grey); letter-spacing: -0.3px;
  }
  .holder .name b { font-weight: 800; }
  .holder .role {
    display: block; font-weight: 700; font-size: 14px;
    color: var(--brand-mid); letter-spacing: 0.5px;
  }
  .rule {
    position: absolute; left: 0; right: 0; top: 207px; height: 4px;
    background: var(--brand-mid);
  }
  .band {
    position: absolute; left: 0; right: 0; top: 216px; bottom: 0;
    background: linear-gradient(180deg, var(--band-top) 0%, var(--brand-deep) 100%);
  }
  .contacts { position: absolute; left: 24px; top: 272px; list-style: none; }
  .contacts li {
    display: flex; align-items: center; gap: 7px;
    height: 22px;
    font-weight: 600; font-size: 15.5px; color: var(--white);
  }
  .contacts svg { width: 16px; height: 16px; flex: none; }
</style>
</head>
<body>
<main class="canvas">

  <section class="card card-front" aria-label="Card front">
    <div class="front-lockup">
      <span class="wordmark">Trevolant</span>
      <span class="tagline">ADVANCING YOUR STRATEGY</span>
    </div>
  </section>

  <section class="card card-back" aria-label="Card back">
    <div class="back-lockup">
      <span class="wordmark">Trevolant</span>
      <span class="tagline">ADVANCING YOUR STRATEGY</span>
    </div>

    <div class="holder">
      <span class="name"><b>Tiago</b>Moreira</span>
      <span class="role">PARTNER</span>
    </div>

    <div class="rule"></div>
    <div class="band"></div>

    <ul class="contacts">
      <li>
        <svg viewBox="0 0 16 16" aria-hidden="true">
          <rect x="4" y="1" width="8" height="14" rx="1.5" fill="none" stroke="#fff" stroke-width="1.6"/>
          <circle cx="8" cy="12.3" r="0.9" fill="#fff"/>
        </svg>
        +351 912 480 317
      </li>
      <li>
        <svg viewBox="0 0 16 16" aria-hidden="true">
          <rect x="1" y="3.5" width="14" height="9.5" fill="#fff"/>
          <path d="M1 3.5 L8 9 L15 3.5 M1 13 L6 8 M15 13 L10 8" fill="none" stroke="#0b5cab" stroke-width="1.2"/>
        </svg>
        tiago.moreira@trevolant.com
      </li>
      <li>
        <svg viewBox="0 0 16 16" aria-hidden="true">
          <circle cx="8" cy="8" r="6.5" fill="#fff"/>
          <path d="M1.5 8 H14.5 M8 1.5 V14.5 M3 4.5 H13 M3 11.5 H13" stroke="#0b5cab" stroke-width="0.9" fill="none"/>
          <ellipse cx="8" cy="8" rx="3" ry="6.5" fill="none" stroke="#0b5cab" stroke-width="0.9"/>
        </svg>
        www.trevolant.com
      </li>
    </ul>
  </section>

</main>
</body>
</html>
```